Cybersecurity company is looking for business card.

I need a business card design for our company, we are a cybersecurity company providing advance technology to protect agains any kind of malware. We need a fresh modern design it should communicate modern, technology and growth.

Target Market(s)

Business to business

Industry/Entity Type

Business

Contact Information for Business Card

Should have location, address, fax, mobile, phone, email and website.

Requirements
Must have
• Must follow company's logo color and style. Must have the company's log on its.

```html
<!DOCTYPE html>
<html lang="en">
<head>
<meta charset="utf-8">
<title>Vantrel Business Card</title>
<link rel="stylesheet" href="https://fonts.googleapis.com/css2?family=Ubuntu:ital,wght@0,400;0,500;0,700;1,400&display=swap">
<style>
  :root {
    --stage: #1c1c1c;
    --card-white: #f4f4f4;
    --card-black: #0e1112;
    --ink: #141414;
    --ink-soft: #3a3a3a;
    --brand-red: #8c1010;
    --brand-red-dark: #6e0b0b;
    --on-red: #ffffff;
  }
  * { margin: 0; padding: 0; box-sizing: border-box; }
  html, body {
    width: 1200px;
    height: 1000px;
    overflow: hidden;
    background: var(--stage);
    font-family: "Ubuntu", sans-serif;
  }
  .stage {
    position: relative;
    width: 1200px;
    height: 1000px;
  }
  .card {
    position: absolute;
    left: 250px;
    width: 700px;
    height: 400px;
    overflow: hidden;
  }
  .card--front { top: 70px; background: linear-gradient(160deg, #ffffff 0%, var(--card-white) 60%, #e9e9e9 100%); }
  .card--back { top: 530px; background: linear-gradient(150deg, #1a1e20 0%, var(--card-black) 70%); }

  .wordmark {
    font-weight: 700;
    letter-spacing: 1px;
    line-height: 1;
    display: flex;
    align-items: center;
    gap: 10px;
  }
  .wordmark__dot { display: block; background: var(--brand-red); }

  .card--front .wordmark {
    position: absolute;
    left: 70px;
    top: 108px;
    font-size: 56px;
    color: var(--ink);
  }
  .card--front .wordmark__dot { width: 14px; height: 14px; }

  .contact {
    position: absolute;
    left: 430px;
    top: 108px;
    font-size: 17px;
    color: var(--ink);
    line-height: 1.5;
  }
  .contact__address { margin-bottom: 8px; }
  .contact__line span { display: inline-block; width: 26px; }

  .holder__tab {
    position: absolute;
    left: 0;
    top: 226px;
    width: 10px;
    height: 36px;
    background: var(--brand-red);
  }
  .holder {
    position: absolute;
    left: 72px;
    top: 224px;
    color: var(--ink-soft);
  }
  .holder__name { font-size: 22px; font-weight: 700; }
  .holder__role { font-size: 17px; margin-top: 2px; }

  .band {
    position: absolute;
    inset: 0;
    background: linear-gradient(90deg, var(--brand-red-dark), var(--brand-red));
    clip-path: polygon(310px 400px, 385px 282px, 700px 282px, 700px 400px);
  }
  .band__text {
    position: absolute;
    left: 470px;
    top: 300px;
    font-size: 17px;
    color: var(--on-red);
    line-height: 1.6;
  }
  .band__text span { display: inline-block; width: 26px; }

  .card--back .wordmark {
    position: absolute;
    left: 50%;
    top: 50%;
    transform: translate(-50%, -50%);
    font-size: 96px;
    color: #f2f2f2;
  }
  .card--back .wordmark__dot { width: 22px; height: 22px; }
</style>
</head>
<body>
<main class="stage">
  <section class="card card--front" aria-label="Business card front">
    <div class="wordmark"><span class="wordmark__dot"></span>vantrel</div>

    <div class="contact">
      <p class="contact__address">your address goes here</p>
      <p class="contact__line"><span>m</span>: +147 5550 19274</p>
      <p class="contact__line"><span>p</span>: 800 0155 50199</p>
      <p class="contact__line"><span>f</span>: 800 0155 50199</p>
    </div>

    <div class="holder__tab"></div>
    <div class="holder">
      <p class="holder__name">Cardholder Name</p>
      <p class="holder__role">CEO &amp; Founder</p>
    </div>

    <div class="band"></div>
    <div class="band__text">
      <p><span>e</span>: emailid@vantrel.com</p>
      <p><span>w</span>: www.vantrel.com</p>
    </div>
  </section>

  <section class="card card--back" aria-label="Business card back">
    <div class="wordmark"><span class="wordmark__dot"></span>vantrel</div>
  </section>
</main>
</body>
</html>
```